Tidy Haven Path half fold brochure design

I need a brochure for a new company. The name of the company is Tidy Haven Path. I am a Professional Organizer. I am requesting a one fold brochure 11" wide x 8.5" high (obviously once folded 5.5" wide x 8.5" high) brochure. I have been told this may need to be designed as a flyer? I have attached a VERY BASIC layout of what I think I am looking for. I have also attached the original logos in all the different formats I have. I would like to have a very light green background & the text I have in orange please make orange. PLEASE feel free to add color to my "Tidy Haven Path" logo's and use light/soft green & orange shades if possible (OK to go darker for BOLD purposes) The brochure DOES NOT have to stick to this layout, again just what I THINK I want :) - THANK YOU

EDIT: 01-21-15 Remove MARLENE KUDSIK from all 3 places (front, bottom inside right & back) Remove just the KUDSIK from the 1st line on the back. PRIVACY & ETHICS on the back, please remove "PRIVACY &", leave Ethics and the 1st line of the text under it. Please remove all of the text following the 1st sentence. THANK YOU

Industry/Entity Type

It Company

```html
<!DOCTYPE html>
<html lang="en">
<head>
<meta charset="UTF-8">
<title>Tidy Haven Path – Inside Spread</title>
<link href="https://fonts.googleapis.com/css2?family=Lato:ital,wght@0,400;0,700;0,900;1,400;1,700&display=swap" rel="stylesheet">
<style>
  :root {
    --backdrop: #d6d6d6;
    --paper: #ffffff;
    --ink: #3a3a3a;
    --orange: #f39a1e;
    --orange-deep: #e8870c;
    --photo-light: #f4f1ee;
    --photo-warm: #e6d9cc;
    --photo-shade: #c9b6a3;
  }
  * { box-sizing: border-box; margin: 0; padding: 0; }
  html, body {
    width: 1200px; height: 800px; overflow: hidden;
    background: var(--backdrop);
    font-family: "Lato", sans-serif;
    color: var(--ink);
  }
  .spread {
    position: absolute; left: 100px; top: 14px;
    width: 1000px; height: 772px;
    display: flex;
    background: var(--paper);
    box-shadow: 0 4px 14px rgba(0,0,0,.18);
  }
  .page { position: relative; width: 500px; height: 100%; overflow: hidden; }
  .page--left { padding: 60px 44px 40px 48px; border-right: 1px solid #ececec; }
  .page--right { padding: 44px 40px 0 36px; }

  .body-text { font-size: 12.5px; line-height: 1.42; margin-bottom: 16px; }
  .question {
    color: var(--orange); font-weight: 700; font-size: 14px;
    margin: 4px 0 8px 14px;
  }
  .answer { margin-left: 14px; }
  .closing {
    color: var(--orange); font-weight: 900; font-size: 19px;
    line-height: 1.2; text-transform: uppercase; margin-top: 22px;
  }

  .section-title { color: var(--orange); font-weight: 700; font-size: 14px; margin-bottom: 8px; }
  .quote { font-size: 12px; line-height: 1.4; margin-bottom: 12px; }
  .quote-source { font-style: italic; }
  .intro { font-size: 12px; line-height: 1.4; margin-bottom: 14px; }

  .services { display: flex; gap: 22px; position: relative; z-index: 2; }
  .services__col { flex: 1; }
  .service { margin-bottom: 10px; }
  .service__label {
    display: inline-block; background: var(--orange); color: #fff;
    font-size: 11px; font-weight: 700; letter-spacing: .5px;
    text-transform: uppercase; padding: 3px 18px 3px 6px; margin-bottom: 4px;
  }
  .service__list { list-style: none; font-size: 11.5px; line-height: 1.35; }
  .service__list li { padding-left: 10px; position: relative; }
  .service__list li::before { content: "•"; position: absolute; left: 0; }
  .contact-note { font-size: 11.5px; font-weight: 700; line-height: 1.35; margin-top: 6px; }

  .family-photo {
    position: absolute; left: 0; right: 0; bottom: 0; height: 380px;
    background:
      radial-gradient(ellipse at 60% 55%, var(--photo-warm) 0%, transparent 60%),
      radial-gradient(ellipse at 35% 80%, var(--photo-shade) 0%, transparent 45%),
      linear-gradient(180deg, rgba(255,255,255,1) 0%, var(--photo-light) 30%, var(--photo-light) 100%);
    z-index: 1;
  }
</style>
</head>
<body>
  <main class="spread">
    <section class="page page--left">
      <p class="body-text">Getting organized isn't <em>all</em> about everything being in its proper place. It can also require overcoming fears and anxieties such as:</p>

      <h3 class="question">“How do I start?”</h3>
      <p class="body-text answer">You begin by getting help from a professional. No one can do everything; everyone needs a helping hand at times. (I bring my vehicle to a mechanic when it needs service, even for just a simple oil change!)</p>

      <h3 class="question">“Am I going to have to get rid of ALL my things?”</h3>
      <p class="body-text answer">Definitely not! There is a process that will help you decide what to keep and what you would be willing to part with. (I can help you determine the practical and monetary “worth” of something. Only you can determine its personal “value.”)</p>

      <h3 class="question">“I don't have time”</h3>
      <p class="body-text answer">Now you will! Getting organized will actually save you time. You will know where that “thing” is, find it quickly and avoid the time it takes to run out and purchase a new “thing”. (You will have actually created more time to enjoy the lifestyle that is important to you.)</p>

      <p class="body-text answer">We all have anxiety about something that prevents or inhibits us from taking action toward a solution. Whether you want someone to take over the project or a helping hand (nudge) is all you really need, a professional organizer is the perfect way to get started. Getting organized is going to be a process of progress, not perfection. It will require some level of support and continued work on you part, but the rewards will far outweigh the efforts.</p>

      <p class="closing answer">Together we can conquer the clutter and create clarity</p>
    </section>

    <section class="page page--right">
      <h2 class="section-title">What is a professional organizer?</h2>
      <p class="quote">“A Professional Organizer enhances the lives of clients by designing systems and processes using organizing principles and through transferring organizing skills. Professional Organizers help individuals and businesses take control of their surroundings, their time, their paper, and their systems for life.” <span class="quote-source">– National Guild of Home Organizers</span></p>
      <p class="intro">Whether you are too busy, too confused, overwhelmed, tired, stressed or just don't know where to start, I offer a variety of hands-on services to help you bring a sense of fun, freedom and functionality to almost any space.</p>

      <div class="services">
        <div class="services__col">
          <div class="service">
            <span class="service__label">Attic – to – Basement</span>
            <ul class="service__list"><li>Sorting – Purging – Organizing</li></ul>
          </div>
          <div class="service">
            <span class="service__label">Paper Control</span>
            <ul class="service__list">
              <li>Sorting – Purging – Organizing</li>
              <li>Household, home office &amp; home based filing systems</li>
            </ul>
          </div>
          <div class="service">
            <span class="service__label">Downsizing</span>
            <ul class="service__list">
              <li>Sorting – Purging – Organizing – Labeling</li>
              <li>Packing &amp; unpacking</li>
            </ul>
          </div>
        </div>
        <div class="services__col">
          <div class="service">
            <span class="service__label">Removal</span>
            <ul class="service__list">
              <li>Light trash &amp; proper disposal</li>
              <li>Donations &amp; light recyclables to proper locations</li>
              <li>Shredding Service</li>
            </ul>
          </div>
          <div class="service">
            <span class="service__label">Follow Up</span>
            <ul class="service__list"><li>Routine “clutter maintenance” visits</li></ul>
          </div>
          <p class="contact-note">For projects not listed above, please contact me.</p>
        </div>
      </div>

      <div class="family-photo" role="img" aria-label="Photo of a smiling family of four relaxing together in a bright white room"></div>
    </section>
  </main>
</body>
</html>
```